Maplebrook Cremations Postcard

Postcards to explain our services. Modern yet professional remembering this is about people's loved one's. Use Poppins font and Century Gothic.

Target Market(s)

People who's loved ones are going to pass away.

Font styles to use
Sans Serif

Colors
33a6d7

Requirements
Must have
• Logo, website, all the information from the attachments.

```html
<!DOCTYPE html>
<html lang="en">
<head>
<meta charset="UTF-8">
<title>Maplebrook Cremations Postcard</title>
<link rel="stylesheet" href="https://fonts.googleapis.com/css2?family=Poppins:wght@400;500;600;700&family=Montserrat:wght@500;600;700&family=Oswald:wght@600&display=swap">
<style>
  :root {
    --blue: #0aa0df;
    --blue-deep: #33a6d7;
    --orange: #f57c14;
    --orange-light: #fbb03b;
    --charcoal: #262626;
    --charcoal-soft: #2e2e2e;
    --white: #ffffff;
    --page: #e9e9e9;
    --stamp: #efefef;
    --ink: #222222;
  }
  * { margin: 0; padding: 0; box-sizing: border-box; }
  html, body { width: 1200px; height: 2594px; overflow: hidden; }
  body { background: var(--page); font-family: "Poppins", sans-serif; position: relative; }

  .postcard {
    position: absolute; left: 131px; width: 940px;
    background: var(--white);
    box-shadow: 0 4px 10px rgba(0,0,0,0.25);
    overflow: hidden;
  }
  .postcard--front { top: 634px; height: 626px; }
  .postcard--back { top: 1332px; height: 628px; }
  .postcard__shapes { position: absolute; inset: 0; }

  /* brand */
  .brand { position: absolute; text-align: center; }
  .brand__dot { display: block; margin: 0 auto; border-radius: 50%; background: var(--orange); }
  .brand__name {
    display: block; font-family: "Montserrat", sans-serif; font-weight: 600;
    color: var(--blue); letter-spacing: 3px; white-space: nowrap;
  }
  .postcard--front .brand { left: 40px; top: 34px; width: 300px; }
  .postcard--front .brand__dot { width: 130px; height: 130px; }
  .postcard--front .brand__name { font-size: 34px; margin-top: 22px; }
  .postcard--back .brand { left: 470px; top: 38px; width: 300px; }
  .postcard--back .brand__dot { width: 86px; height: 86px; }
  .postcard--back .brand__name { font-size: 24px; margin-top: 14px; }

  /* front */
  .offer { position: absolute; left: 36px; top: 246px; display: flex; align-items: center; gap: 20px; }
  .offer__price {
    font-family: "Oswald", sans-serif; font-weight: 600; font-size: 106px; line-height: 1;
    color: var(--orange); letter-spacing: -2px;
  }
  .offer__label { font-weight: 700; font-size: 40px; line-height: 1.05; color: var(--white); }
  .pill {
    position: absolute; left: 25px; top: 374px; height: 44px; padding: 0 16px;
    background: var(--orange); border-radius: 22px; border: 2px solid var(--white);
    color: var(--white); font-weight: 600; font-size: 21px; line-height: 40px;
    font-family: "Montserrat", sans-serif;
  }
  .delivery { position: absolute; left: 27px; top: 448px; }
  .delivery__lead { font-family: "Montserrat", sans-serif; font-weight: 500; font-size: 19px; color: var(--ink); }
  .delivery__area { font-weight: 700; font-size: 38px; line-height: 1.1; color: var(--orange); }
  .delivery__rule { width: 54px; height: 3px; background: var(--orange); margin-top: 4px; }

  .contact-phone {
    position: absolute; display: flex; align-items: center; gap: 14px;
    font-family: "Montserrat", sans-serif; font-weight: 700; white-space: nowrap;
  }
  .postcard--front .contact-phone { left: 38px; top: 564px; font-size: 40px; color: var(--orange); }
  .front-web {
    position: absolute; right: 44px; top: 588px;
    font-family: "Montserrat", sans-serif; font-weight: 600; font-size: 15px;
    color: var(--white); letter-spacing: 0.3px; text-transform: uppercase;
  }

  /* back */
  .services { position: absolute; left: 48px; top: 26px; }
  .services__title {
    font-family: "Montserrat", sans-serif; font-weight: 700; font-size: 33px;
    color: var(--orange); letter-spacing: 0.5px; margin-bottom: 10px;
  }
  .services__list { list-style: none; }
  .services__item {
    display: flex; gap: 10px; color: var(--white);
    font-family: "Montserrat", sans-serif; font-weight: 500; font-size: 20px; line-height: 24px;
    margin-bottom: 12px;
  }
  .services__item svg { flex: none; margin-top: 5px; }
  .back-contact { position: absolute; left: 52px; top: 540px; color: var(--white); }
  .postcard--back .contact-phone { position: static; font-size: 34px; gap: 10px; }
  .back-web {
    display: flex; align-items: center; gap: 14px; margin-top: 6px;
    font-family: "Montserrat", sans-serif; font-weight: 600; font-size: 15px; text-transform: uppercase;
  }
  .stamp { position: absolute; left: 783px; top: 33px; width: 117px; height: 117px; background: var(--stamp); }
</style>
</head>
<body>

<section class="postcard postcard--front">
  <svg class="postcard__shapes" width="940" height="626" viewBox="0 0 940 626">
    <defs>
      <linearGradient id="sea" x1="0" y1="0" x2="0" y2="1">
        <stop offset="0" stop-color="#f9b52a"/>
        <stop offset="0.35" stop-color="#f6a21c"/>
        <stop offset="0.4" stop-color="#e87a10"/>
        <stop offset="0.8" stop-color="#f08a1a"/>
        <stop offset="1" stop-color="#d9661a"/>
      </linearGradient>
    </defs>
    <path d="M548 0 Q448 310 528 626 L940 626 L940 0 Z" fill="url(#sea)" role="img" aria-label="Photograph of a golden sunset over the sea and beach"/>
    <path d="M532 0 Q430 310 512 626" fill="none" stroke="var(--orange)" stroke-width="12"/>
    <rect x="0" y="552" width="560" height="74" fill="var(--charcoal)"/>
    <polygon points="528,572 940,572 940,626 548,626" fill="var(--orange)"/>
    <polygon points="0,233 482,233 470,393 0,393" fill="var(--blue)"/>
  </svg>

  <div class="brand">
    <span class="brand__dot"></span>
    <span class="brand__name">MAPLEBROOK</span>
  </div>

  <div class="offer">
    <span class="offer__price">$695</span>
    <span class="offer__label">All<br>Inclusive</span>
  </div>
  <div class="pill">Online Arrangement Center</div>

  <div class="delivery">
    <p class="delivery__lead">Hand Delivery of Cremated Remains</p>
    <p class="delivery__area">Miami-Dade County</p>
    <div class="delivery__rule"></div>
  </div>

  <div class="contact-phone">
    <svg width="38" height="36" viewBox="0 0 38 36" fill="none" stroke="var(--white)" stroke-width="2.5">
      <path d="M3 12 Q19 0 35 12 L31 16 L25 13 L25 9 Q19 7 13 9 L13 13 L7 16 Z"/>
      <path d="M11 16 L27 16 L33 33 L5 33 Z"/>
      <circle cx="19" cy="25" r="4"/>
    </svg>
    <span>(305) 555-0142</span>
  </div>
  <div class="front-web">www.maplebrookcremations.com</div>
</section>

<section class="postcard postcard--back">
  <svg class="postcard__shapes" width="940" height="628" viewBox="0 0 940 628">
    <path d="M0 0 L410 0 Q530 250 490 540 L0 540 Z" fill="var(--charcoal-soft)"/>
    <path d="M420 0 Q545 250 500 540" fill="none" stroke="var(--blue)" stroke-width="8"/>
    <path d="M0 612 L470 612 L464 628 L0 628 Z" fill="var(--charcoal)"/>
    <polygon points="0,533 486,533 448,618 0,618" fill="var(--blue)"/>
  </svg>

  <div class="services">
    <h2 class="services__title">OUR SERVICE</h2>
    <ul class="services__list">
      <li class="services__item"><svg width="16" height="16" viewBox="0 0 16 16" fill="none" stroke="var(--orange)" stroke-width="1.4"><circle cx="8" cy="8" r="7"/><path d="M4.5 8.2 L7 10.5 L11.5 5.5"/></svg><span>Filing Death Certificate</span></li>
      <li class="services__item"><svg width="16" height="16" viewBox="0 0 16 16" fill="none" stroke="var(--orange)" stroke-width="1.4"><circle cx="8" cy="8" r="7"/><path d="M4.5 8.2 L7 10.5 L11.5 5.5"/></svg><span>Bringing Your Loved One<br>into our Care</span></li>
      <li class="services__item"><svg width="16" height="16" viewBox="0 0 16 16" fill="none" stroke="var(--orange)" stroke-width="1.4"><circle cx="8" cy="8" r="7"/><path d="M4.5 8.2 L7 10.5 L11.5 5.5"/></svg><span>Refrigeration</span></li>
      <li class="services__item"><svg width="16" height="16" viewBox="0 0 16 16" fill="none" stroke="var(--orange)" stroke-width="1.4"><circle cx="8" cy="8" r="7"/><path d="M4.5 8.2 L7 10.5 L11.5 5.5"/></svg><span>Crematory Fee</span></li>
      <li class="services__item"><svg width="16" height="16" viewBox="0 0 16 16" fill="none" stroke="var(--orange)" stroke-width="1.4"><circle cx="8" cy="8" r="7"/><path d="M4.5 8.2 L7 10.5 L11.5 5.5"/></svg><span>Alternative Container (Cardboard)</span></li>
      <li class="services__item"><svg width="16" height="16" viewBox="0 0 16 16" fill="none" stroke="var(--orange)" stroke-width="1.4"><circle cx="8" cy="8" r="7"/><path d="M4.5 8.2 L7 10.5 L11.5 5.5"/></svg><span>Temporary Container (Cardboard)</span></li>
      <li class="services__item"><svg width="16" height="16" viewBox="0 0 16 16" fill="none" stroke="var(--orange)" stroke-width="1.4"><circle cx="8" cy="8" r="7"/><path d="M4.5 8.2 L7 10.5 L11.5 5.5"/></svg><span>Hand Delivery of Cremated Remains<br>Miami-Dade County</span></li>
      <li class="services__item"><svg width="16" height="16" viewBox="0 0 16 16" fill="none" stroke="var(--orange)" stroke-width="1.4"><circle cx="8" cy="8" r="7"/><path d="M4.5 8.2 L7 10.5 L11.5 5.5"/></svg><span>Medical Examiner Cremation<br>Approval Fee</span></li>
      <li class="services__item"><svg width="16" height="16" viewBox="0 0 16 16" fill="none" stroke="var(--orange)" stroke-width="1.4"><circle cx="8" cy="8" r="7"/><path d="M4.5 8.2 L7 10.5 L11.5 5.5"/></svg><span>1st Copy of Death Certificate</span></li>
      <li class="services__item"><svg width="16" height="16" viewBox="0 0 16 16" fill="none" stroke="var(--orange)" stroke-width="1.4"><circle cx="8" cy="8" r="7"/><path d="M4.5 8.2 L7 10.5 L11.5 5.5"/></svg><span>Online Guestbook</span></li>
    </ul>
  </div>

  <div class="back-contact">
    <div class="contact-phone">
      <svg width="30" height="28" viewBox="0 0 38 36" fill="none" stroke="var(--white)" stroke-width="2.5">
        <path d="M3 12 Q19 0 35 12 L31 16 L25 13 L25 9 Q19 7 13 9 L13 13 L7 16 Z"/>
        <path d="M11 16 L27 16 L33 33 L5 33 Z"/>
        <circle cx="19" cy="25" r="4"/>
      </svg>
      <span>(305) 555-0142</span>
    </div>
    <div class="back-web">
      <svg width="26" height="26" viewBox="0 0 26 26" fill="none" stroke="var(--white)" stroke-width="1.8">
        <circle cx="13" cy="13" r="11"/><ellipse cx="13" cy="13" rx="5" ry="11"/>
        <path d="M2 13 H24 M4 7 H22 M4 19 H22"/>
      </svg>
      <span>www.maplebrookcremations.com</span>
    </div>
  </div>

  <div class="brand">
    <span class="brand__dot"></span>
    <span class="brand__name">MAPLEBROOK</span>
  </div>
  <div class="stamp"></div>
</section>

</body>
</html>
```